Wine Bottle Label for Tall Fern Cellars

We are a small, newly established winery in need of an original, bold and outstanding bottle label design for our Tall Fern wine.

Our vineyard and winery are located on a 200 acre farm in a remote part of southern Oregon. The name "Tall Fern" was inspired by the large, overgrown size of all of the foliage here, including our grapevines. Things grow large and vigorous in Oregon! And everything is very lush and green. It is almost surreal or other-worldly, like the landscapes seen in the Keeper of The Stones movies, or the land of Quill. It is a place that makes you say "wow" with its epic, large scale, natural beauty.

The name "Tall Fern" also captures the essence of our wine. It is big in flavor, quality and color. Our first release is a Pinot Noir (red). Pinot Noir wines often are subtle in flavor and thin in their color. Our label should convey that our Pinot Noir is a much more robust, darker, heavier, meatier, more flavorful wine that is a lot more fun than an "ordinary" wine. At the same time, this wine is not cheap, and so nothing in the label should convey "bargain," "low price," or "cheapness." This is a fine wine with a sense of adventure. Be sure to convey "quality" with your design along with "big," "adventure" and "fun".

The label should appeal to a younger demographic, both male and female, between the ages of 21 and 35. It should be non-traditional and adventurous and suggest a pushing of boundaries and a breaking of rules. This Pinot Noir does not conform to the normal "limitations" of the variety, therefore the label should not conform. It should have an "organic" or "natural" or "agricultural" vibe, as opposed to something mechanical or technical. It should, however, be contemporary. Do not confuse "natural" or "organic" with being nostalgic or old school. Think "agri-hipsters."

The label should be designed to fit on a Burgundy-style wine bottle (photo attached for reference). (Note: All Pinot Noir and Chardonnay is bottled in Burgundy bottles, If you are not sure about the bottle shape you can go to a local store and compare the various bottles. Locate a bottle of Pinot Noir or Chardonnay or anything identified as a "Burgundy Wine," and it should be the correct bottle. The tall, skinny bottles used for Cabernet Sauvignon are NOT correct)). Please see the "Must Have" notes for more on the bottle.

In summary, the final project should be a wine bottle label design that conveys bigness, vastness, adventurous, non-traditional, high quality wine. A good tagline to keep in mind is "Living Large."

Target Market(s)

Young, hip, non-conformist wine drinkers aged 21-35 with a sense of adventure and an appreciation of quality.

Requirements
Must have
• *Must contain the words:

Tall Fern (the brand)
2013 Pinot Noir (the vintage year and variety)

*The label must be designed to fit a Burgundy-style wine bottle. A photo is attached for reference.

*Additionally, the label needs to fit on the lower, widest part of the bottle. The label will be printed on sticky paper and rolled onto the bottle with a machine. The machine cannot apply labels to the neck of the bottle. The maximum size of a label that will fit this space is 5.5 inches wide by 4.5 inches tall. You DO NOT have to fill ALL of this space or confine the label shape to a rectangle, but the label cannot exceed this size or it won't stick to the bottle properly. It will really help if you can put your hands on an actual bottle to see the logistics of applying the label. But if that is not possible, just do your best with the instructions you have. I am confident the winning design could be adjusted to fit the bottle, if necessary
Nice to have
• *Wine grape leaf or leaves.

*A concept I have been playing with is sunlight shining through leaves like light through a Harwick lamp or a stained glass window. This is NOT a requirement for this label. However, if the concept inspires and idea, I would be most happy to see it.
Should not have
• IF a leaf or leaves are included in the design (not a requirement) they MUST be wine grapevine leafs and preferably leaves of the Pinot Noir vine. Do not use generic leaves or identifiable leaves such as oak leaves, maple leaves, or anything that looks like the Canadian flag or the Duluth Granite Hawks hockey logo. Reference the attached photos of wine grape leaves to see the correct leaf type. I am happy to email more photos upon request. These photos may be used in whole or in part in your design, however, a leaf from a photo is NOT a requirement, nor is the image of a leaf or leaves.

This label should NOT be designed for Bordeaux-style wine bottles (the tall, skinny ones).

```html
<!DOCTYPE html>
<html lang="en">
<head>
<meta charset="utf-8">
<title>Tall Fern Pinot Noir Label</title>
<link href="https://fonts.googleapis.com/css2?family=Big+Shoulders+Inline+Display:wght@600&family=Oswald:wght@500&family=Pathway+Gothic+One&display=swap" rel="stylesheet">
<style>
  :root {
    --wine-red: #800203;
    --parchment: #e8e3d5;
    --page: #ffffff;
  }
  html, body {
    margin: 0;
    padding: 0;
    width: 1200px;
    height: 997px;
    overflow: hidden;
    background: var(--page);
  }
  .label {
    position: relative;
    width: 1200px;
    height: 997px;
  }
  .label-art {
    position: absolute;
    inset: 0;
  }
  .label-text {
    position: absolute;
    margin: 0;
    color: var(--parchment);
    white-space: nowrap;
    line-height: 1;
  }
  .region {
    font-family: "Oswald", sans-serif;
    font-weight: 500;
    font-size: 31px;
    letter-spacing: 4px;
    top: 220px;
  }
  .region-town { left: 251px; }
  .region-state { right: 268px; }
  .vintage {
    font-family: "Oswald", sans-serif;
    font-weight: 500;
    font-size: 46px;
    letter-spacing: 2px;
    top: 444px;
  }
  .vintage-century { left: 284px; }
  .vintage-year { right: 305px; }
  .brand-name {
    font-family: "Big Shoulders Inline Display", sans-serif;
    font-weight: 600;
    font-size: 96px;
    letter-spacing: 17px;
    left: 0;
    width: 1200px;
    text-align: center;
    top: 424px;
    text-indent: 17px;
  }
  .variety {
    font-family: "Oswald", sans-serif;
    font-weight: 500;
    font-size: 30px;
    letter-spacing: 5px;
    color: var(--wine-red);
    left: 0;
    width: 1200px;
    text-align: center;
    top: 536px;
  }
  .fine-print {
    font-family: "Pathway Gothic One", sans-serif;
    font-size: 24px;
    top: 734px;
  }
  .alcohol { left: 252px; }
  .volume { right: 272px; }
</style>
</head>
<body>
<main class="label">
  <svg class="label-art" width="1200" height="997" viewBox="0 0 1200 997" aria-hidden="false">
    <path class="label-body" fill="var(--wine-red)"
      d="M232 167 H948 A37 37 0 0 0 985 204 V775 A37 37 0 0 0 948 812 H232 A37 37 0 0 0 195 775 V204 A37 37 0 0 0 232 167 Z"/>
    <path class="label-frame" fill="none" stroke="var(--parchment)" stroke-width="2.5"
      d="M242 177 H938 A47 47 0 0 0 975 214 V765 A47 47 0 0 0 938 802 H242 A47 47 0 0 0 205 765 V214 A47 47 0 0 0 242 177 Z"/>
    <path class="leaf-area" role="img" aria-label="Illustration of a large grapevine leaf with its stem"
      fill="var(--parchment)"
      d="M590 405 C560 300 460 290 420 340 C360 380 350 470 360 540 C365 610 420 640 470 660 C520 700 560 740 590 775 C620 740 660 700 710 660 C760 640 815 610 820 540 C830 470 820 380 760 340 C720 290 620 300 590 405 Z"/>
    <rect class="title-band" x="275" y="419" width="631" height="104" fill="var(--wine-red)"/>
    <line class="title-rule" x1="275" y1="419" x2="906" y2="419" stroke="var(--parchment)" stroke-width="2.5"/>
    <line class="title-rule" x1="275" y1="523" x2="906" y2="523" stroke="var(--parchment)" stroke-width="2.5"/>
  </svg>

  <p class="label-text region region-town">ELKTON</p>
  <p class="label-text region region-state">OREGON</p>

  <p class="label-text vintage vintage-century">20</p>
  <h1 class="label-text brand-name">TALL FERN</h1>
  <p class="label-text vintage vintage-year">13</p>

  <p class="label-text variety">-PINOT NOIR-</p>

  <p class="label-text fine-print alcohol">ALC. 12.5% BY VOL.</p>
  <p class="label-text fine-print volume">750 ML ℮</p>
</main>
</body>
</html>
```